Wageline Associates Business Card Design

We need a business card designed around our new logo. The business card should be modern in design & should communicate success, confidence, power, sophistication. The target market is young business professionals. This is for a human resource & payroll outsourcing business.

```html
<!DOCTYPE html>
<html lang="en">
<head>
<meta charset="utf-8">
<title>Wageline Associates — Business Card</title>
<link rel="stylesheet" href="https://fonts.googleapis.com/css2?family=Lora:ital,wght@0,400;0,600;1,400&display=swap">
<style>
  :root {
    --backdrop: #24272b;
    --card-black: #141414;
    --card-white: #ffffff;
    --accent-red: #d81e1e;
    --text-white: #f2f2f2;
    --text-grey: #d6d6d6;
    --mark-grey: #8c8c8c;
  }
  * { margin: 0; padding: 0; box-sizing: border-box; }
  html, body { width: 1200px; height: 900px; overflow: hidden; }
  body {
    background: var(--backdrop);
    font-family: "Lora", Georgia, serif;
    position: relative;
  }
  .card {
    position: absolute;
    top: 295px;
    width: 540px;
    height: 310px;
    border-radius: 26px;
    background: var(--card-black);
    overflow: hidden;
    box-shadow: 0 18px 40px rgba(0,0,0,0.45);
  }
  .card--front { left: 40px; }
  .card--back { left: 620px; }

  .front-curve { position: absolute; inset: 0; width: 540px; height: 310px; }

  .contact-block {
    position: absolute;
    left: 292px;
    top: 92px;
    color: var(--text-grey);
  }
  .holder-name {
    font-size: 27px;
    font-weight: 400;
    color: var(--text-white);
    line-height: 1.1;
  }
  .holder-title {
    font-size: 13px;
    font-style: italic;
    color: var(--accent-red);
    margin-top: 2px;
    margin-bottom: 14px;
  }
  .contact-line {
    display: flex;
    align-items: center;
    gap: 9px;
    font-size: 14px;
    line-height: 1.55;
  }
  .contact-icon { width: 12px; height: 12px; flex: none; }
  .social-row {
    display: flex;
    align-items: center;
    gap: 10px;
    margin-top: 14px;
    margin-left: -50px;
    font-size: 14px;
  }
  .social-label { margin-right: 6px; }
  .social-square {
    width: 17px;
    height: 17px;
    border-radius: 3px;
    background: var(--accent-red);
  }

  .brand-lockup {
    position: absolute;
    inset: 0;
    display: flex;
    align-items: center;
    justify-content: center;
    gap: 14px;
  }
  .brand-dot {
    width: 22px;
    height: 22px;
    border-radius: 50%;
    background: var(--accent-red);
  }
  .brand-name {
    font-size: 38px;
    font-weight: 600;
    color: var(--mark-grey);
  }
</style>
</head>
<body>

  <section class="card card--front">
    <svg class="front-curve" viewBox="0 0 540 310" aria-hidden="true">
      <path d="M0 0 H250 C228 130 150 240 0 272 Z" fill="var(--card-white)"/>
      <path d="M250 0 C228 130 150 240 0 272 L0 300 C170 268 252 150 272 0 Z" fill="var(--accent-red)"/>
    </svg>

    <div class="contact-block">
      <h1 class="holder-name">Your Name</h1>
      <p class="holder-title">Job Title</p>
      <p class="contact-line">
        <svg class="contact-icon" viewBox="0 0 12 12" aria-hidden="true"><path d="M2 1 L4.5 1 L5.5 3.8 L4 5 C4.8 6.6 5.6 7.4 7 8 L8.2 6.5 L11 7.5 L11 10 C11 10.6 10.5 11 10 11 C5 11 1 7 1 2 C1 1.5 1.4 1 2 1 Z" fill="var(--accent-red)"/></svg>
        000 000 0000
      </p>
      <p class="contact-line">
        <svg class="contact-icon" viewBox="0 0 12 12" aria-hidden="true"><rect x="0.5" y="2" width="11" height="8" rx="1" fill="var(--accent-red)"/><path d="M1 2.5 L6 6.5 L11 2.5" stroke="var(--card-black)" stroke-width="1" fill="none"/></svg>
        youremail@xyz.com
      </p>
      <p class="contact-line">
        <svg class="contact-icon" viewBox="0 0 12 12" aria-hidden="true"><circle cx="6" cy="6" r="5" fill="none" stroke="var(--accent-red)" stroke-width="1.2"/><ellipse cx="6" cy="6" rx="2.2" ry="5" fill="none" stroke="var(--accent-red)" stroke-width="1"/><line x1="1" y1="6" x2="11" y2="6" stroke="var(--accent-red)" stroke-width="1"/></svg>
        www.yourwebsite.com
      </p>
      <div class="social-row">
        <span class="social-label">Find Us on :</span>
        <span class="social-square"></span>
        <span class="social-square"></span>
        <span class="social-square"></span>
        <span class="social-square"></span>
      </div>
    </div>
  </section>

  <section class="card card--back">
    <div class="brand-lockup">
      <span class="brand-dot"></span>
      <span class="brand-name">Wageline Associates</span>
    </div>
  </section>

</body>
</html>
```